letterhead design using our existing logo

We are a small boutique property management business based in Sydney's Northern Beaches.
We are after a sleek, simple modern letterhead (A4) incorporating our logo and its colours.
Also matching envelope (DL)
I have attached the logo with black text and white text for design options.

Target Market(s)

29-69yo Male and Female

Industry/Entity Type

Property Management

Requirements
Must have
• - Keyhaven Estates logo
• - Address, number and website:
• Suite 7, 18-19 Harlow Parade, Brookvale NSW 2100
• Tel: Tom Carrick 0417 293 608 Lorena Adcock 0409 516 742 www.keyhavenestatesgroup.com.au
Nice to have
• sleek design that looks modern and professional
Should not have
• too many colours or too busy

```html
<!DOCTYPE html>
<html lang="en">
<head>
<meta charset="utf-8">
<title>Keyhaven Estates Stationery</title>
<link rel="stylesheet" href="https://fonts.googleapis.com/css2?family=Open+Sans:wght@400;600;700&family=Arimo:wght@400;700&display=swap">
<style>
  :root {
    --teal: #247785;
    --teal-light: #3a9499;
    --teal-dark: #1f6c79;
    --ink: #262626;
    --paper: #f6f6f6;
    --backdrop: #e8e8e8;
    --card-dark: #25292b;
    --white: #ffffff;
  }
  * { margin: 0; padding: 0; box-sizing: border-box; }
  html, body { width: 1200px; height: 795px; overflow: hidden; }
  body { background: var(--backdrop); position: relative; font-family: "Arimo", Arial, sans-serif; }
  .sheet { position: absolute; background: var(--paper); }
  .brand { position: absolute; font-family: "Open Sans", Arial, sans-serif; font-weight: 700; text-transform: uppercase; color: var(--ink); white-space: nowrap; letter-spacing: -0.2px; }
  .band { position: absolute; background: var(--teal); color: var(--white); }
  .stub { position: absolute; background: var(--teal); }
  .phone-icon { width: 5px; height: 5px; vertical-align: -0.5px; margin-right: 2px; fill: currentColor; }

  /* Letterhead */
  .letterhead { left: 292px; top: 99px; width: 293px; height: 415px; }
  .letterhead .stub { left: 0; top: 20px; width: 4px; height: 32px; }
  .letterhead .brand { left: 17px; top: 31px; font-size: 9.5px; }
  .letterhead .band { left: 110px; top: 20px; width: 183px; height: 32px; padding: 3px 0 0 119px; font-size: 5px; line-height: 6.6px; }
  .letterhead .band strong { font-weight: 700; }
  .letterhead .band p + p { margin-top: 2px; }
  .letterhead-footer { position: absolute; left: 0; right: 0; top: 392px; text-align: center; font-size: 4.6px; line-height: 7px; color: #666; }
  .letterhead-footer b { color: var(--teal); }

  /* Presentation folder */
  .folder { position: absolute; left: 636px; top: 80px; width: 346px; height: 437px;
    background: radial-gradient(ellipse at 50% 47%, var(--teal-light) 0%, var(--teal) 55%, var(--teal-dark) 100%); }
  .folder-spine { position: absolute; left: 0; top: 0; width: 24px; height: 100%; border-right: 1px solid rgba(0,0,0,0.08); }
  .folder .brand { left: 0; right: 0; top: 187px; text-align: center; font-size: 25px; font-weight: 600; }

  /* Business cards */
  .card { position: absolute; width: 132px; height: 76px; }
  .card-front { left: 186px; top: 550px; background: var(--paper); }
  .card-front .stub { left: 0; top: 26px; width: 2px; height: 22px; }
  .card-front .brand { left: 8px; top: 34px; font-size: 6.2px; }
  .card-details { position: absolute; left: 68px; top: 20px; font-size: 3.4px; line-height: 4.8px; color: #555; }
  .card-details .name { color: var(--teal); font-weight: 700; font-size: 4.6px; margin-bottom: 1px; }
  .card-details .gap { margin-top: 2px; }
  .card-back { left: 186px; top: 647px; background: var(--card-dark); }
  .card-back .brand { left: 0; right: 0; top: 31px; text-align: center; font-size: 7.8px; font-weight: 600; color: var(--white); }

  /* DL envelope front */
  .envelope-front { left: 354px; top: 562px; width: 328px; height: 156px; }
  .envelope-front .stub { left: 0; top: 12px; width: 3px; height: 33px; }
  .envelope-front .brand { left: 9px; top: 22px; font-size: 9.5px; }
  .envelope-front .band { left: 104px; top: 12px; width: 224px; height: 33px; padding: 7px 0 0 9px; font-size: 4.8px; line-height: 6.2px; }

  /* DL envelope back */
  .envelope-back { left: 714px; top: 562px; width: 327px; height: 156px; }
  .envelope-flap { position: absolute; left: 0; top: 0; width: 327px; height: 56px; }
  .envelope-back .brand { left: 0; right: 0; top: 23px; text-align: center; font-size: 7px; font-weight: 600; color: var(--white); }
</style>
</head>
<body>

  <section class="sheet letterhead" aria-label="A4 letterhead">
    <div class="stub"></div>
    <div class="brand">Keyhaven Estates</div>
    <div class="band">
      <p><strong>Tom Carrick</strong><br>
        <svg class="phone-icon" viewBox="0 0 10 10"><path d="M2 0.5l2 2-1 1.3c.6 1.2 1.6 2.2 2.8 2.8L7 5.5l2 2-1.2 1.7C4.3 9 1 5.7.8 2.2z"/></svg>0417 293 608</p>
      <p><strong>Lorena Adcock</strong><br>
        <svg class="phone-icon" viewBox="0 0 10 10"><path d="M2 0.5l2 2-1 1.3c.6 1.2 1.6 2.2 2.8 2.8L7 5.5l2 2-1.2 1.7C4.3 9 1 5.7.8 2.2z"/></svg>0409 516 742</p>
    </div>
    <footer class="letterhead-footer">
      <p>Suite 7, 18-19 Harlow Parade, Brookvale NSW 2100</p>
      <p><b>E</b> : info@keyhavenestatesgroup.com.au &nbsp;|&nbsp; <b>W</b> : www.keyhavenestatesgroup.com.au</p>
    </footer>
  </section>

  <section class="folder" aria-label="Presentation folder cover">
    <div class="folder-spine"></div>
    <div class="brand">Keyhaven Estates</div>
  </section>

  <section class="card card-front" aria-label="Business card front">
    <div class="stub"></div>
    <div class="brand">Keyhaven Estates</div>
    <div class="card-details">
      <p class="name">Tom Carrick</p>
      <p>Suite 7</p>
      <p>18-19 Harlow Parade</p>
      <p>Brookvale NSW 2100</p>
      <p class="gap">0417 293 608</p>
      <p>tom@keyhavenestatesgroup.com.au</p>
      <p>www.keyhavenestatesgroup.com.au</p>
    </div>
  </section>

  <section class="card card-back" aria-label="Business card back">
    <div class="brand">Keyhaven Estates</div>
  </section>

  <section class="sheet envelope-front" aria-label="DL envelope front">
    <div class="stub"></div>
    <div class="brand">Keyhaven Estates</div>
    <div class="band">
      <p>Suite 7</p>
      <p>18-19 Harlow Parade</p>
      <p>Brookvale NSW 2100</p>
    </div>
  </section>

  <section class="sheet envelope-back" aria-label="DL envelope back">
    <svg class="envelope-flap" viewBox="0 0 327 56" aria-hidden="true">
      <defs>
        <radialGradient id="flapGradient" cx="50%" cy="40%" r="60%">
          <stop offset="0" stop-color="#3a9499"/>
          <stop offset="1" stop-color="#237483"/>
        </radialGradient>
      </defs>
      <path d="M0 0H327L322 46Q321 55 312 55H15Q6 55 5 46Z" fill="url(#flapGradient)"/>
    </svg>
    <div class="brand">Keyhaven Estates</div>
  </section>

</body>
</html>
```